Coffeeshop menu for filter tip

We want to have a cannabis (coffeeshop) menu in the size 25mm wide x 60mm wide. Some examples attached.

it must have the following text:
Menu

WEED p/g
Velotrine €16
Cinderfox €14
Tide Rambler €14
Marigolden €16
Grand Pelican €14
Copper Comet €14

HASH p/g
Baltic Ember €12
Harbor Velvet€11
Plum Rova €14
Dusk Maple €10

Target Market(s)

tourist in Amsterdam

Requirements
Nice to have
• cannabis sign leaf
• No Cigarettes allowed symbol

```html
<!DOCTYPE html>
<html lang="en">
<head>
<meta charset="utf-8">
<title>Coffeeshop Menu</title>
<link rel="stylesheet" href="https://fonts.googleapis.com/css2?family=Roboto:ital,wght@0,300;1,300&display=swap">
<style>
  :root {
    --page: #ffffff;
    --panel: #1d1f1e;
    --panel-light: #2b2e2c;
    --label-band: #4a504c;
    --ink: #ffffff;
    --accent: #8cc152;
    --leaf-badge: #2e9c48;
    --warning: #d0202a;
  }
  * { margin: 0; padding: 0; box-sizing: border-box; }
  html, body { width: 1200px; height: 2334px; overflow: hidden; background: var(--page); }
  body { font-family: "Roboto", Arial, sans-serif; font-weight: 300; color: var(--ink); position: relative; }

  .menu-card {
    position: absolute; left: 150px; top: 105px; width: 888px; height: 2130px;
    background: var(--panel); overflow: hidden;
  }
  .leaf-texture {
    position: absolute; inset: 0;
    background: radial-gradient(ellipse at 30% 25%, var(--panel-light) 0%, var(--panel) 55%),
                radial-gradient(ellipse at 75% 70%, var(--panel-light) 0%, transparent 50%);
    background-blend-mode: lighten;
  }
  .menu-title {
    position: absolute; top: 60px; left: 0; right: 0; text-align: center;
    font-size: 168px; line-height: 1; color: var(--accent); letter-spacing: 2px;
  }
  .section-head { position: absolute; left: 0; right: 0; height: 105px; }
  .section-label {
    position: absolute; left: 0; top: 0; width: 360px; height: 105px;
    background: var(--label-band); padding-left: 54px;
    font-size: 92px; line-height: 105px;
  }
  .section-unit {
    position: absolute; right: 51px; top: 0; font-size: 92px; line-height: 105px;
  }
  .price-list { position: absolute; left: 54px; right: 51px; list-style: none; }
  .price-row {
    display: flex; justify-content: space-between; align-items: center;
    height: 105px; font-size: 84px; line-height: 105px;
  }
  .leaf-badge { position: absolute; left: 360px; top: 1131px; width: 168px; height: 168px; }
  .house-rule {
    position: absolute; left: 162px; top: 1992px; display: flex; align-items: center; gap: 39px;
  }
  .house-rule-text { font-size: 66px; font-style: italic; color: var(--accent); }
</style>
</head>
<body>
  <main class="menu-card">
    <div class="leaf-texture" role="img" aria-label="Faint dark cannabis leaf pattern across the background"></div>

    <h1 class="menu-title">MENU</h1>

    <div class="section-head" style="top:315px">
      <span class="section-label">WEED</span>
      <span class="section-unit">p/g</span>
    </div>
    <ul class="price-list" style="top:436px">
      <li class="price-row"><span>Velotrine</span><span>€16</span></li>
      <li class="price-row"><span>Cinderfox</span><span>€14</span></li>
      <li class="price-row"><span>Tide Rambler</span><span>€14</span></li>
      <li class="price-row"><span>Marigolden</span><span>€16</span></li>
      <li class="price-row"><span>Grand Pelican</span><span>€14</span></li>
      <li class="price-row"><span>Copper Comet</span><span>€14</span></li>
    </ul>

    <svg class="leaf-badge" viewBox="0 0 168 168" role="img" aria-label="Cannabis leaf sign in a green circle">
      <circle cx="84" cy="84" r="82" fill="var(--ink)"/>
      <circle cx="84" cy="84" r="74" fill="var(--leaf-badge)"/>
    </svg>

    <div class="section-head" style="top:1365px">
      <span class="section-label">HASH</span>
      <span class="section-unit">p/g</span>
    </div>
    <ul class="price-list" style="top:1486px">
      <li class="price-row"><span>Baltic Ember</span><span>€12</span></li>
      <li class="price-row"><span>Harbor Velvet</span><span>€11</span></li>
      <li class="price-row"><span>Plum Rova</span><span>€14</span></li>
      <li class="price-row"><span>Dusk Maple</span><span>€10</span></li>
    </ul>

    <div class="house-rule">
      <svg width="96" height="96" viewBox="0 0 96 96" aria-label="No smoking">
        <circle cx="48" cy="48" r="44" fill="var(--ink)"/>
        <rect x="16" y="44" width="52" height="12" fill="var(--ink)" stroke="#555" stroke-width="2"/>
        <rect x="68" y="44" width="14" height="12" fill="#e08a2c"/>
        <path d="M72 40 q4 -8 0 -16" stroke="#888" stroke-width="3" fill="none"/>
        <circle cx="48" cy="48" r="40" fill="none" stroke="var(--warning)" stroke-width="9"/>
        <line x1="20" y1="20" x2="76" y2="76" stroke="var(--warning)" stroke-width="9"/>
      </svg>
      <span class="house-rule-text">No Cigarettes</span>
    </div>
  </main>
</body>
</html>
```